Business Card Design for Massage Therapist

*I am a qualified massage therapist & require a business card for my new business 'Tidal Bodywork & Wellness'.
*Contact details I'd like included on the card are: Hester Pradley, Mobile: 0481539260, Email: tidalbw@quillpost.com
*It is a massage business dedicated to providing quality therapeutic massage treatments, that will later incorporate natural therapies.
* Styles Include: Swedish, Relaxation, Pregnancy, Deep Tissue & Sports Massage
*I offer the styles of massage as listed above & a mobile service that allows clients to book a massage in the comfort of their own home.
*I'd like my logo to be fairly simple, streamlined, modern & reflect what my business services are - one people will easily remember.
*I'd like the colors to represent & emit a sense of calm, be fresh, welcoming, natural colors that appeal to a wide range of people.
*Colors I'd like to see are: pale blue, aqua & greens.

Target Market(s)

Both Male & Female, aged 20 to 65, singles, couples, parents, business people who are interested in their health, fitness & general wellbeing and maintenance. Located in the Fernvale area and surrounding suburbs of Melbourne.

Industry/Entity Type

Massage

Requirements
Must have
• Fonts used in logos should be owned by the designer.
Should not have
• I don't want the design to have someone being massaged in it (pictures/photos) or have it look too clinical & sterile.

```html
<!DOCTYPE html>
<html lang="en">
<head>
<meta charset="utf-8">
<title>Tidal Bodywork &amp; Wellness – Business Card</title>
<link rel="stylesheet" href="https://fonts.googleapis.com/css2?family=Tinos&display=swap">
<style>
  :root {
    --page: #ffffff;
    --ink: #1a1a1a;
    --card-edge: #222222;
    --aqua-band: #93dfec;
    --mint-disc: #b3fbd9;
    --fresh-green: #2ef072;
    --band-text: #ffffff;
  }
  * { margin: 0; padding: 0; box-sizing: border-box; }
  html, body {
    width: 832px; height: 1200px; overflow: hidden;
    background: var(--page);
  }
  body {
    position: relative;
    font-family: "Tinos", "Times New Roman", serif;
    color: var(--ink);
  }
  .card {
    position: absolute;
    left: 37px; width: 754px;
    border: 1px solid var(--card-edge);
    background: var(--page);
    overflow: hidden;
  }
  .card--front { top: 43px; height: 533px; }
  .card--back { top: 615px; height: 533px; }

  .accent-line { position: absolute; }
  .accent-line--top {
    left: 10px; top: 5px; width: 735px; height: 3px;
    background: linear-gradient(to right, var(--fresh-green) 70%, rgba(46,240,114,0.2));
  }
  .accent-line--left {
    left: 10px; top: 5px; width: 3px; height: 515px;
    background: linear-gradient(to bottom, var(--fresh-green) 70%, rgba(46,240,114,0.2));
  }
  .accent-line--right {
    right: 6px; top: 14px; width: 3px; height: 512px;
    background: linear-gradient(to top, var(--fresh-green) 70%, rgba(46,240,114,0.2));
  }
  .accent-line--bottom {
    right: 6px; bottom: 6px; width: 735px; height: 3px;
    background: linear-gradient(to left, var(--fresh-green) 70%, rgba(46,240,114,0.2));
  }

  .brand-disc {
    position: absolute;
    border-radius: 50%;
    background: var(--mint-disc);
  }
  .card--front .brand-disc { left: 376px; top: 96px; width: 322px; height: 322px; }
  .card--back .brand-disc { left: 602px; top: 10px; width: 134px; height: 134px; }

  .band {
    position: absolute;
    background: var(--aqua-band);
    color: var(--band-text);
    display: flex; align-items: center;
    white-space: nowrap;
    font-weight: 400;
  }
  .band--brand-large {
    left: 55px; top: 173px; width: 453px; height: 70px;
    padding-left: 18px; font-size: 27px;
  }
  .band--brand-small {
    left: 468px; top: 45px; width: 185px; height: 26px;
    padding-left: 7px; font-size: 10.5px;
  }
  .band--name {
    left: 17px; top: 206px; width: 387px; height: 46px;
    padding-left: 10px; font-size: 27px;
  }

  .role {
    position: absolute; left: 27px; top: 256px;
    font-size: 14px; letter-spacing: 0.2px;
  }
  .services {
    position: absolute; left: 27px; top: 293px;
    list-style: none; font-size: 14px; line-height: 20px;
  }
  .contact {
    position: absolute; right: 17px; top: 474px;
    text-align: right; font-size: 16.5px; line-height: 22px;
    letter-spacing: 0.3px;
  }
</style>
</head>
<body>
  <section class="card card--front" aria-label="Card front">
    <span class="accent-line accent-line--top"></span>
    <span class="accent-line accent-line--left"></span>
    <div class="brand-disc"></div>
    <div class="band band--brand-large">TIDAL BODYWORK &amp; WELLNESS</div>
  </section>

  <section class="card card--back" aria-label="Card back">
    <span class="accent-line accent-line--right"></span>
    <span class="accent-line accent-line--bottom"></span>
    <div class="brand-disc"></div>
    <div class="band band--brand-small">TIDAL BODYWORK &amp; WELLNESS</div>

    <div class="band band--name">HESTER PRADLEY</div>
    <p class="role">MASSAGE THERAPIST</p>
    <ul class="services">
      <li>SWEDISH</li>
      <li>RELAXATION</li>
      <li>PREGNANCY</li>
      <li>DEEP TISSUE</li>
      <li>SPORTS MASSAGE</li>
    </ul>
    <div class="contact">
      <p>MOBILE: 0481 539 260</p>
      <p>E-MAIL: tidalbw@quillpost.com</p>
    </div>
  </section>
</body>
</html>
```